We need 3 A2 posters similar look but different enough to be eye catching when changed.

We are a healthcare centre that requires 3 A2 posters - simple, similar but different background colours. These posters will be used within our business to promote services we provide to our clients.

The design should include our logo(attached), a large header and a large section in the middle of the poster to promote the event. We need a blank text box (which WE can insert text to advertise), and 1 image to advertise the event. Please note, we do not need you to choose an image we simply would like you to place a demo to give us an idea of where it should sit.

We want to use the bubble design (attached) as a background and the company colours pink, orange and blue - as on our website. Attached is a copy of our logo and background bubble effect. You can also refer to our website - www.tallowparkwellness.com.au for more inspiration.

Just to reiterate, these posters should be simple, different but have a uniform feel. They should have an empty middle section that can be edited to add text and a space for an eye catching title and matching image.

Our services include Chiropractic, Podiatry, Nutrition, Massage, Yoga, Pilates and Specialised rehabilitation classes.

Reason: Hi designers, I know we are all busy but I really need more designs from the designers I invited to this project and look forward to receiving more designs. Any questions please let me know. Regards, Marnie

Reason: Hi all Increased the budget Regards Marnie

Corporate Sydney City office workers

Healthcare

• logo and company colours
section in the middles that can be edited to add text
Space allocated for image placement
Catchy title/header

```html
<!DOCTYPE html>
<html lang="en">
<head>
<meta charset="utf-8">
<title>Tallow Park Wellness – Poster Series</title>
<link rel="stylesheet" href="https://fonts.googleapis.com/css2?family=Open+Sans:ital,wght@0,400;0,600;0,700;1,700&family=Tinos&display=swap">
<style>
  :root {
    --orange: #e8801f;
    --orange-soft: #f7cba2;
    --blue: #0b7cc5;
    --blue-soft: #a8d2ef;
    --pink: #b4196d;
    --pink-soft: #e9a6cb;
    --brand-blue: #1f74c8;
    --ink: #1d1d1d;
    --grey-text: #8a8a8a;
    --bubble: #ececec;
    --frame: #d4d4d4;
    --sans: "Open Sans", Arial, sans-serif;
    --serif: "Tinos", "Times New Roman", serif;
  }
  * { box-sizing: border-box; margin: 0; padding: 0; }
  html, body { width: 1200px; height: 537px; overflow: hidden; background: #ffffff; }
  .series { position: relative; width: 1200px; height: 537px; overflow: hidden; }

  .poster {
    position: absolute; top: 0; width: 392px; height: 588px;
    transform: scale(0.9133); transform-origin: 0 0;
    background: #fff; border: 1px solid var(--frame); overflow: hidden;
    font-family: var(--sans); color: var(--ink);
  }
  .poster--orange { left: 0;   --accent: var(--orange); --accent-soft: var(--orange-soft); }
  .poster--blue   { left: 413px; --accent: var(--blue);   --accent-soft: var(--blue-soft); }
  .poster--pink   { left: 840px; --accent: var(--pink);   --accent-soft: var(--pink-soft); }

  .abs { position: absolute; }
  .shapes { position: absolute; left: 0; top: 0; width: 392px; height: 588px; }

  .bubbles { position: absolute; background: linear-gradient(180deg, #f4f4f4, var(--bubble)); opacity: .8; }

  .brand-bar { left: 0; top: 0; width: 355px; height: 46px; background: var(--brand-blue); display: flex; align-items: center; padding-left: 14px; }
  .brand-name { font-family: var(--sans); font-weight: 700; font-size: 19px; color: #fff; }

  .edge { right: 0; width: 12px; }
  .edge--pink { top: 0; height: 62px; background: var(--pink); }
  .edge--orange-top { top: 62px; height: 48px; background: var(--orange); }
  .edge--blue { top: 425px; height: 80px; background: var(--blue); }
  .edge--orange-bottom { top: 515px; height: 50px; background: var(--orange); }

  .intro-tag { left: 0; top: 73px; width: 205px; height: 20px; background: var(--accent); color: var(--ink); font-size: 15px; line-height: 20px; padding-left: 5px; }
  .poster--blue .intro-tag, .poster--pink .intro-tag { color: #fff; }
  .headline { left: 0; width: 392px; top: 90px; text-align: center; font-size: 35px; font-weight: 400; color: #fff; letter-spacing: -1px; padding-right: 24px; }
  .people-bar { left: 5px; top: 133px; width: 235px; height: 24px; background: var(--accent); color: #fff; font-size: 17px; line-height: 24px; text-align: right; padding-right: 6px; }
  .city { left: 244px; top: 126px; font-size: 28px; color: var(--ink); letter-spacing: -.5px; }

  .photo-slot { width: 105px; height: 88px; border: 1px solid var(--accent); border-radius: 10px; background: linear-gradient(135deg, #e9e6e3, #9a938d 70%, #3a3a3a); }
  .leaf { width: 18px; height: 18px; border-radius: 3px; background: linear-gradient(135deg, var(--accent-soft), var(--accent)); }

  .serif { font-family: var(--serif); white-space: nowrap; }
  .nature { font-size: 23px; color: var(--ink); }
  .keep { font-size: 33px; color: var(--grey-text); }
  .fit { font-size: 45px; color: var(--accent); }

  .benefit { width: 160px; font-size: 8px; line-height: 10.5px; color: var(--ink); padding-left: 5px; border-left: 3px solid var(--pink); }
  .benefit--short { border-left-color: var(--orange); }
  .benefit--blue { border-left-color: var(--blue); }
  .benefit + .benefit { margin-top: 3px; }

  .service { background: var(--accent); color: #fff; font-size: 10.5px; font-weight: 600; padding: 2px 5px; line-height: 13px; box-shadow: 3px 3px 3px rgba(0,0,0,.3); white-space: nowrap; }
  .service--wide { white-space: normal; width: 74px; }
  .services-title { left: 143px; top: 452px; width: 108px; height: 17px; background: #fff; border: 1px solid #bbb; font-size: 12px; font-weight: 700; font-style: italic; letter-spacing: 2px; text-align: center; line-height: 15px; }

  .footer { left: 0; bottom: 0; width: 392px; height: 22px; background: var(--accent); color: #fff; font-size: 10.5px; font-weight: 700; font-style: italic; letter-spacing: 3.2px; line-height: 22px; padding-left: 6px; white-space: nowrap; }
</style>
</head>
<body>
<main class="series">

  <!-- Orange poster -->
  <article class="poster poster--orange">
    <div class="abs bubbles" role="img" aria-label="Soft grey bubble background" style="left:0;top:40px;width:380px;height:130px"></div>
    <div class="abs bubbles" role="img" aria-label="Soft grey bubble background" style="left:0;top:420px;width:380px;height:145px"></div>
    <svg class="shapes" viewBox="0 0 392 588" aria-hidden="true">
      <polygon points="0,170 380,170 190,40" fill="var(--accent-soft)"/>
      <polygon points="0,420 380,420 195,568" fill="var(--accent-soft)"/>
    </svg>
    <div class="abs brand-bar"><span class="brand-name">Tallow Park Wellness</span></div>
    <div class="abs edge edge--pink"></div><div class="abs edge edge--orange-top"></div>
    <div class="abs edge edge--blue"></div><div class="abs edge edge--orange-bottom"></div>

    <div class="abs intro-tag">Some of our</div>
    <h1 class="abs headline">special doctors</h1>
    <div class="abs people-bar">are for the people</div>
    <div class="abs city">in Sydney</div>

    <div class="abs photo-slot" role="img" aria-label="Demo photo: woman in a yoga stretch" style="left:32px;top:195px"></div>
    <p class="abs serif nature" style="left:185px;top:198px">Nature therapies</p>
    <p class="abs serif keep" style="left:162px;top:230px">to keep you</p>
    <p class="abs serif fit" style="left:128px;top:278px">fit and fine</p>

    <div class="abs leaf" role="img" aria-label="Small autumn leaf" style="left:185px;top:333px"></div>
    <div class="abs leaf" role="img" aria-label="Small autumn leaf" style="left:32px;top:392px"></div>
    <div class="abs" style="left:45px;top:343px">
      <p class="benefit">Is run by health professionals, making sure you stay injury free and achieve your maximum potential during your workouts</p>
      <p class="benefit benefit--short">Will always have a limited number of participants per class</p>
    </div>
    <div class="abs" style="left:207px;top:343px">
      <p class="benefit benefit--blue">Has only the best instructors in Sydney, selected for their education, knowledge, experience and ability</p>
      <p class="benefit">Boasts an extensive timetable with convenient options designed to suit all availabilities</p>
    </div>

    <span class="abs service" style="left:40px;top:426px">Chiropractic</span>
    <span class="abs service" style="left:66px;top:452px">Podiatry</span>
    <span class="abs service" style="left:96px;top:484px">Nutrition</span>
    <span class="abs service" style="left:291px;top:428px">Massage</span>
    <span class="abs service" style="left:291px;top:460px">Yoga</span>
    <span class="abs service" style="left:263px;top:488px">Pilates</span>
    <span class="abs service service--wide" style="left:160px;top:508px">Specialised rehabilitation classes</span>
    <div class="abs services-title">Our services</div>
    <div class="abs footer">One place for a complete health solution</div>
  </article>

  <!-- Blue poster -->
  <article class="poster poster--blue">
    <div class="abs bubbles" role="img" aria-label="Soft grey bubble background" style="left:0;top:40px;width:380px;height:130px"></div>
    <div class="abs bubbles" role="img" aria-label="Soft grey bubble background" style="left:0;top:420px;width:380px;height:145px"></div>
    <svg class="shapes" viewBox="0 0 392 588" aria-hidden="true">
      <polygon points="0,170 380,170 190,40" fill="var(--accent-soft)"/>
      <polygon points="0,420 380,420 195,568" fill="var(--accent-soft)"/>
    </svg>
    <div class="abs brand-bar"><span class="brand-name">Tallow Park Wellness</span></div>
    <div class="abs edge edge--pink"></div><div class="abs edge edge--orange-top"></div>
    <div class="abs edge edge--blue"></div><div class="abs edge edge--orange-bottom"></div>

    <div class="abs intro-tag">Some of our</div>
    <h1 class="abs headline">special doctors</h1>
    <div class="abs people-bar">are for the people</div>
    <div class="abs city">in Sydney</div>

    <div class="abs photo-slot" role="img" aria-label="Demo photo: woman in a yoga stretch" style="left:213px;top:195px"></div>
    <p class="abs serif nature" style="left:9px;top:198px">Nature therapies</p>
    <p class="abs serif keep" style="left:9px;top:230px">to keep you</p>
    <p class="abs serif fit" style="left:128px;top:278px">fit and fine</p>

    <div class="abs leaf" role="img" aria-label="Small autumn leaf" style="left:188px;top:333px"></div>
    <div class="abs leaf" role="img" aria-label="Small autumn leaf" style="left:30px;top:392px"></div>
    <div class="abs" style="left:45px;top:343px">
      <p class="benefit">Is run by health professionals, making sure you stay injury free and achieve your maximum potential during your workouts</p>
      <p class="benefit benefit--short">Will always have a limited number of participants per class</p>
    </div>
    <div class="abs" style="left:207px;top:343px">
      <p class="benefit benefit--blue">Has only the best instructors in Sydney, selected for their education, knowledge, experience and ability</p>
      <p class="benefit">Boasts an extensive timetable with convenient options designed to suit all availabilities</p>
    </div>

    <span class="abs service" style="left:40px;top:426px">Chiropractic</span>
    <span class="abs service" style="left:66px;top:452px">Podiatry</span>
    <span class="abs service" style="left:96px;top:484px">Nutrition</span>
    <span class="abs service" style="left:291px;top:428px">Massage</span>
    <span class="abs service" style="left:291px;top:460px">Yoga</span>
    <span class="abs service" style="left:263px;top:488px">Pilates</span>
    <span class="abs service service--wide" style="left:160px;top:508px">Specialised rehabilitation classes</span>
    <div class="abs services-title">Our services</div>
    <div class="abs footer">One place for a complete health solution</div>
  </article>

  <!-- Pink poster -->
  <article class="poster poster--pink">
    <div class="abs bubbles" role="img" aria-label="Soft grey bubble background" style="left:0;top:40px;width:380px;height:130px"></div>
    <div class="abs bubbles" role="img" aria-label="Soft grey bubble background" style="left:0;top:420px;width:380px;height:145px"></div>
    <svg class="shapes" viewBox="0 0 392 588" aria-hidden="true">
      <polygon points="0,170 380,170 190,40" fill="var(--accent-soft)"/>
      <polygon points="0,420 380,420 195,568" fill="var(--accent-soft)"/>
    </svg>
    <div class="abs brand-bar"><span class="brand-name">Tallow Park Wellness</span></div>
    <div class="abs edge edge--pink"></div><div class="abs edge edge--orange-top"></div>
    <div class="abs edge edge--blue"></div><div class="abs edge edge--orange-bottom"></div>

    <div class="abs intro-tag">Some of our</div>
    <h1 class="abs headline">special doctors</h1>
    <div class="abs people-bar">are for the people</div>
    <div class="abs city">in Sydney</div>

    <p class="abs serif nature" style="left:5px;top:175px;color:var(--grey-text)">Nature therapies to keep you</p>
    <div class="abs leaf" role="img" aria-label="Small autumn leaf" style="left:188px;top:210px"></div>
    <div class="abs leaf" role="img" aria-label="Small autumn leaf" style="left:35px;top:248px"></div>
    <div class="abs" style="left:50px;top:212px">
      <p class="benefit">Is run by health professionals, making sure you stay injury free and achieve your maximum potential during your workouts</p>
      <p class="benefit benefit--short">Will always have a limited number of participants per class</p>
    </div>
    <div class="abs" style="left:210px;top:210px">
      <p class="benefit benefit--blue">Has only the best instructors in Sydney, selected for their education, knowledge, experience and ability</p>
      <p class="benefit">Boasts an extensive timetable with convenient options designed to suit all availabilities</p>
    </div>

    <div class="abs photo-slot" role="img" aria-label="Demo photo: woman in a yoga stretch" style="left:108px;top:287px"></div>
    <p class="abs serif fit" style="left:85px;top:366px">fit and fine</p>

    <span class="abs service" style="left:40px;top:426px">Chiropractic</span>
    <span class="abs service" style="left:66px;top:452px">Podiatry</span>
    <span class="abs service" style="left:96px;top:484px">Nutrition</span>
    <span class="abs service" style="left:291px;top:428px">Massage</span>
    <span class="abs service" style="left:291px;top:460px">Yoga</span>
    <span class="abs service" style="left:263px;top:488px">Pilates</span>
    <span class="abs service service--wide" style="left:160px;top:508px">Specialised rehabilitation classes</span>
    <div class="abs services-title">Our services</div>
    <div class="abs footer">One place for a complete health solution</div>
  </article>

</main>
</body>
</html>
```